Bramwell Hockey Academy

We are are Ice Hockey Development Company that provided on-ice Hockey development services. We need a Landing Page with tabs to direct to individual program pages.
Landing Page
About Page
Winter Program Page
Spring Program Page
Summer Program Page
Team Page
Tournament Page

```html
<!DOCTYPE html>
<html lang="en">
<head>
<meta charset="utf-8">
<title>Bramwell Hockey Academy</title>
<link href="https://fonts.googleapis.com/css2?family=Krona+One&family=Roboto:wght@400;500;700&display=swap" rel="stylesheet">
<style>
:root{
  --green:#1e8a1e;
  --green-dark:#0f6a10;
  --green-deep:#0b5a0b;
  --ink:#111;
  --text:#555;
  --navy:#0f1e2c;
  --white:#fff;
  --head:"Krona One",sans-serif;
  --body:"Roboto",Arial,sans-serif;
}
*{margin:0;padding:0;box-sizing:border-box}
html,body{width:1200px;height:4428px;overflow:hidden;background:#fff}
body{position:relative;font-family:var(--body);color:var(--text)}
.abs{position:absolute}
.btn{position:absolute;display:flex;align-items:center;justify-content:center;background:var(--green);color:#fff;font-family:var(--head);font-size:12px;letter-spacing:.3px;text-decoration:none;box-shadow:0 2px 4px rgba(0,0,0,.25)}
.btn.ghost{background:transparent;border:2px solid #fff;box-shadow:none}
.btn.dark{background:var(--green-deep);box-shadow:0 3px 6px rgba(0,0,0,.35)}
.h2{font-family:var(--head);font-size:28px;line-height:1.3;color:var(--green)}
.copy{font-size:12.5px;line-height:19px;color:var(--text)}
.photo{position:absolute}
.frame{position:absolute;border:2px solid var(--green)}

/* header */
.site-header{left:0;top:0;width:1200px;height:118px;background:#fff}
.brand{left:124px;top:36px;font-family:var(--head);font-size:22px;line-height:26px;color:var(--ink)}
.nav{left:380px;top:82px;display:flex;gap:40px;font-family:var(--body);font-weight:700;font-size:12px;color:#222}
.call{left:850px;top:20px;width:233px;height:40px;font-size:14px}

/* hero */
.hero{left:0;top:118px;width:1200px;height:675px;background:radial-gradient(ellipse at 70% 20%,#6b7b92 0%,#2b3547 40%,#1a2130 60%,#c9d3dc 75%,#e3e9ee 100%)}
.hero-title{left:520px;top:330px;width:650px;text-align:center;font-family:var(--head);font-size:48px;line-height:54px;color:#fff}

/* about */
.about{left:0;top:793px;width:1200px;height:344px;background:linear-gradient(90deg,#22922a,#107010)}

/* spring band */
.spring-band{left:0;top:1676px}
/* tournament */
.tourney{left:0;top:2772px}
.count{left:420px;top:3028px;width:350px;display:flex;justify-content:center;gap:14px;color:var(--green);font-family:var(--body);font-size:32px;font-weight:500}
.count span.sep{font-size:30px}
.count-labels{left:420px;top:3066px;width:350px;display:flex;justify-content:center;gap:38px;color:var(--green);font-size:15px}

/* team */
.card{position:absolute;top:3582px;width:250px;height:350px;background:#fff;border:1px solid #e1e1e1;box-shadow:0 1px 4px rgba(0,0,0,.08)}
.card .pic{height:160px;background:linear-gradient(#f2f2f2,#e6e6e6)}
.card h3{font-family:var(--head);font-size:13px;color:var(--ink);margin:18px 0 0 30px}
.card p{font-size:10.5px;line-height:15px;color:#777;margin:8px 26px 0 30px}
.card .btn{left:30px;top:288px;width:118px;height:32px;font-size:10px}

/* footer */
.site-footer{left:0;top:4068px;width:1200px;height:360px;background:#000;color:#fff}
.f-label{font-family:var(--head);font-size:12px;color:#fff}
.social{display:flex;gap:13px}
.social i{display:block;width:36px;height:36px;border-radius:50%;background:#fff}
</style>
</head>
<body>

<header class="abs site-header">
  <div class="abs brand">BRAMWELL<br>HOCKEY</div>
  <nav class="abs nav" style="left:379px"><span>ABOUT</span><span>WINTER PROGRAM</span><span>SPRING PROGRAM</span><span>SUMMER PROGRAM</span><span>TEAM</span><span>TOURNAMENT</span></nav>
  <a class="btn call">CALL_ 555 014 2207</a>
</header>

<section class="abs hero" role="img" aria-label="Ice hockey player handling the puck on a lit arena rink"></section>
<h1 class="abs hero-title">BRAMWELL HOCKEY ACADEMY</h1>
<a class="btn" style="left:778px;top:463px;width:139px;height:49px">READ MORE</a>

<section class="abs about"></section>
<h2 class="abs h2" style="left:150px;top:903px;color:#fff;font-size:30px;line-height:37px">ABOUT BRAMWELL<br>HOCKEY ACADEMY</h2>
<p class="abs copy" style="left:617px;top:890px;width:440px;color:#fff">Lorem ipsum dolor sit amet, consectetur adipiscing elit, sed do eiusmod tempor incididunt ut labore et dolore magna aliqua. Quis ipsum suspe ndis se ultrices gravida. Risus commodo viverra maecenas accumsan lacus vel facilisis. Lorem ipsum dolor sit amet, consectetur adipiscing elit, sed do eiusmod tempor incididunt ut labore et dolore magna aliqua.</p>
<a class="btn dark" style="left:620px;top:1010px;width:140px;height:50px">READ MORE</a>

<!-- winter -->
<h2 class="abs h2" style="left:145px;top:1278px">WINTER PROGRAM</h2>
<p class="abs copy" style="left:149px;top:1334px;width:440px">Lorem ipsum dolor sit amet, consectetur adipiscing elit, sed do eiusmod tempor incididunt ut labore et dolore magna aliqua. Quis ipsum suspe ndis se ultrices gravida. Risus commodo viverra maecenas accumsan lacus vel facilisis. Lorem ipsum dolor sit amet, consectetur adipiscing elit, sed do eiusmod tempor incididunt ut labore et dolore magna aliqua. Quis ipsum suspe ndisse ultrices gravida. Risus commodo viverra maecenas accum san lacus vel facilisis.</p>
<a class="btn" style="left:149px;top:1483px;width:140px;height:50px">READ MORE</a>
<div class="frame" style="left:662px;top:1268px;width:458px;height:334px"></div>
<div class="photo" style="left:642px;top:1248px;width:458px;height:333px;background:linear-gradient(135deg,#1d3a63,#6a8fb8 50%,#dfe8f0)" role="img" aria-label="Goalie diving as an attacker shoots on net"></div>

<!-- spring -->
<svg class="abs spring-band" width="1200" height="606" viewBox="0 0 1200 606"><defs><linearGradient id="sg" x1="0" x2="1"><stop offset="0" stop-color="#22922a"/><stop offset="1" stop-color="#0f6a10"/></linearGradient></defs><polygon points="0,0 1200,74 1200,530 0,604" fill="url(#sg)"/></svg>
<div class="frame" style="left:85px;top:1840px;width:458px;height:330px;border-color:#fff"></div>
<div class="photo" style="left:102px;top:1815px;width:456px;height:334px;background:linear-gradient(180deg,#3e6b3a,#8fa86a 50%,#c9c18a)" role="img" aria-label="Field hockey players running with sticks on a turf pitch"></div>
<h2 class="abs h2" style="left:618px;top:1855px;color:#fff">SPRING PROGRAM</h2>
<p class="abs copy" style="left:622px;top:1910px;width:440px;color:#fff">Lorem ipsum dolor sit amet, consectetur adipiscing elit, sed do eiusmod tempor incididunt ut labore et dolore magna aliqua. Quis ipsum suspe ndis se ultrices gravida. Risus commodo viverra maecenas accumsan lacus vel facilisis. Lorem ipsum dolor sit amet, consectetur adipiscing elit, sed do eiusmod tempor incididunt ut labore et dolore magna aliqua. Quis ipsum suspe ndisse ultrices gravida. Risus commodo viverra maecenas accum san lacus vel facilisis.</p>
<a class="btn ghost" style="left:622px;top:2058px;width:141px;height:50px">READ MORE</a>

<!-- summer -->
<h2 class="abs h2" style="left:145px;top:2385px">SUMMER PROGRAM</h2>
<p class="abs copy" style="left:149px;top:2441px;width:440px">Lorem ipsum dolor sit amet, consectetur adipiscing elit, sed do eiusmod tempor incididunt ut labore et dolore magna aliqua. Quis ipsum suspe ndis se ultrices gravida. Risus commodo viverra maecenas accumsan lacus vel facilisis. Lorem ipsum dolor sit amet, consectetur adipiscing elit, sed do eiusmod tempor incididunt ut labore et dolore magna aliqua. Quis ipsum suspe ndisse ultrices gravida. Risus commodo viverra maecenas accum san lacus vel facilisis.</p>
<a class="btn" style="left:149px;top:2590px;width:140px;height:50px">READ MORE</a>
<div class="frame" style="left:662px;top:2375px;width:458px;height:334px"></div>
<div class="photo" style="left:642px;top:2355px;width:458px;height:333px;background:linear-gradient(160deg,#1f3552,#6f8fb3 45%,#e4ebf2)" role="img" aria-label="Skater carrying the puck through falling snow"></div>

<!-- tournament -->
<svg class="abs tourney" width="1200" height="563" viewBox="0 0 1200 563"><defs><linearGradient id="tg" x1="0" y1="0" x2="0" y2="1"><stop offset="0" stop-color="#13263a"/><stop offset=".6" stop-color="#0f2030"/><stop offset="1" stop-color="#2a2a30"/></linearGradient></defs><polygon points="0,0 1200,48 1200,563 0,563" fill="url(#tg)"/></svg>
<div class="photo" style="left:150px;top:3020px;width:200px;height:350px;background:linear-gradient(#e7e2cf,#d6b53a)" role="img" aria-label="Player in white and gold jersey skating with stick"></div>
<div class="photo" style="left:820px;top:3030px;width:200px;height:345px;background:linear-gradient(#c8cdd3,#c0262a)" role="img" aria-label="Player in red jersey skating with stick"></div>
<h2 class="abs h2" style="left:0;width:1200px;text-align:center;top:2885px;color:#fff;font-size:30px">TOURNAMENT</h2>
<svg class="abs" style="left:556px;top:2941px" width="76" height="76"><circle cx="38" cy="38" r="36" fill="none" stroke="#2a9a2e" stroke-width="2"/><circle cx="38" cy="38" r="27" fill="#1e8a1e"/><text x="38" y="45" text-anchor="middle" font-family="Krona One,sans-serif" font-size="17" fill="#fff">VS</text></svg>
<div class="abs count"><span>32</span><span class="sep">:</span><span>28</span><span class="sep">:</span><span>54</span><span class="sep">:</span><span>06</span></div>
<div class="abs count-labels"><span>Days</span><span>Hours</span><span>Minutes</span><span>Seconds</span></div>
<p class="abs copy" style="left:400px;top:3108px;width:400px;text-align:center;color:#fff;font-size:11.5px;line-height:16px">Lorem ipsum dolor sit amet, consectetur adipiscing elit, sed do eiusmod tempor incididunt ut labore et dolore magna aliqua is ipsum suspendisse ultrices gravida. Risus commodo viverra maecenas accumsa</p>
<a class="btn" style="left:530px;top:3185px;width:140px;height:45px">BOOK NOW</a>
<svg class="abs" style="left:534px;top:3377px" width="20" height="10"><ellipse cx="10" cy="5" rx="9" ry="4" fill="#222"/></svg>

<!-- team -->
<h2 class="abs h2" style="left:0;width:1200px;text-align:center;top:3505px;font-size:30px">OUR TEAM</h2>
<svg class="abs" style="left:110px;top:3655px" width="28" height="40"><polyline points="22,4 6,20 22,36" fill="none" stroke="#111" stroke-width="4"/></svg>
<svg class="abs" style="left:1044px;top:3655px" width="28" height="40"><polyline points="6,4 22,20 6,36" fill="none" stroke="#111" stroke-width="4"/></svg>
<div class="card" style="left:187px"><div class="pic" role="img" aria-label="Team player portrait"></div><h3>DEVIN MARSH</h3><p>Lorem ipsum dolor sit amet, conse ctetur adipiscing elit, sed do eiusmod tempor incididunt ut labore et dolore magna aliqua. Quis ipsum</p><a class="btn">VIEW PROFILE</a></div>
<div class="card" style="left:466px"><div class="pic" role="img" aria-label="Team player portrait"></div><h3>DEVIN MARSH</h3><p>Lorem ipsum dolor sit amet, conse ctetur adipiscing elit, sed do eiusmod tempor incididunt ut labore et dolore magna aliqua. Quis ipsum</p><a class="btn">VIEW PROFILE</a></div>
<div class="card" style="left:744px"><div class="pic" role="img" aria-label="Team player portrait"></div><h3>DEVIN MARSH</h3><p>Lorem ipsum dolor sit amet, conse ctetur adipiscing elit, sed do eiusmod tempor incididunt ut labore et dolore magna aliqua. Quis ipsum</p><a class="btn">VIEW PROFILE</a></div>

<!-- footer -->
<footer class="abs site-footer">
  <div class="abs" style="left:0;width:1200px;top:60px;text-align:center;font-family:var(--head);font-size:24px;line-height:30px">BRAMWELL<br>HOCKEY</div>
  <div class="abs f-label" style="left:217px;top:197px">ADDRESS</div>
  <p class="abs" style="left:217px;top:222px;font-size:12.5px;line-height:17px;color:#fff">123 Ipsum is simply dummy<br>text of theprintin</p>
  <div class="abs" style="left:440px;top:195px;width:1px;height:55px;background:#555"></div>
  <div class="abs f-label" style="left:487px;top:197px">NEED ANY HELP?</div>
  <div class="abs" style="left:487px;top:220px;font-family:var(--head);font-size:20px;color:var(--green)">(555) 0148 3316</div>
  <div class="abs" style="left:750px;top:195px;width:1px;height:55px;background:#555"></div>
  <div class="abs f-label" style="left:786px;top:197px">FOLLOW US</div>
  <div class="abs social" style="left:782px;top:225px"><i></i><i></i><i></i><i></i></div>
  <p class="abs" style="left:0;width:1200px;text-align:center;top:305px;font-size:12.5px;color:#fff">© 2023 All Rights Reserved | Bramwell Hockey Academy.</p>
</footer>

</body>
</html>
```